Pest Control Company needs business card!

Hi there, we need a business card designed for our new Pest Control Company. Ideally this card will be simple, yet feel elegant and high end. We want to use the colours Orange, Black and White. Please see our attached logo for the exact colours.

Business card details:

Phone - 0461 275 804
Name - Gavin Holloway
Email - Info@steadfastverminguard.com.au

We would also like to include the following list with dot points:

SERVICES / INSPECTIONS

Termites, Wood Borers, Ants, Cockroaches, Spiders, Fleas, Mice, Rats, Bed Bugs, & More!

```html
<!DOCTYPE html>
<html lang="en">
<head>
<meta charset="utf-8">
<title>Steadfast Vermin Guard – Business Card</title>
<link href="https://fonts.googleapis.com/css2?family=Saira+Condensed:wght@300;400;500;600;700&display=swap" rel="stylesheet">
<style>
  :root {
    --canvas: #f1f1f3;
    --orange: #f47b20;
    --black: #231f20;
    --white: #ffffff;
    --grey: #6b6b6b;
    --alert-red: #e8202a;
  }
  * { margin: 0; padding: 0; box-sizing: border-box; }
  html, body { width: 1200px; height: 1000px; overflow: hidden; }
  body {
    background: var(--canvas);
    font-family: "Saira Condensed", "Arial Narrow", sans-serif;
    color: var(--black);
    position: relative;
  }
  .side-label {
    position: absolute;
    top: 296px;
    width: 473px;
    text-align: center;
    font-size: 30px;
    font-weight: 400;
    letter-spacing: 6px;
  }
  .side-label--front { left: 100px; }
  .side-label--back { left: 627px; }

  .card {
    position: absolute;
    top: 359px;
    width: 473px;
    height: 270px;
    overflow: hidden;
  }
  .card--front { left: 100px; background: var(--black); }
  .card--back { left: 627px; background: var(--white); }
  .card__shape { position: absolute; inset: 0; }

  /* front */
  .brand-name {
    position: absolute;
    left: 74px;
    top: 72px;
    width: 170px;
    font-size: 40px;
    line-height: 38px;
    font-weight: 700;
    color: var(--black);
    text-transform: uppercase;
  }
  .brand-mascot {
    position: absolute;
    left: 238px;
    top: 58px;
    width: 132px;
    height: 156px;
    border-radius: 46% 46% 40% 40%;
    background: radial-gradient(circle at 45% 45%, #3a3536 0%, var(--black) 70%);
  }
  .front-phone {
    position: absolute;
    left: 413px;
    top: 135px;
    transform: translate(-50%, -50%) rotate(90deg);
    white-space: nowrap;
    font-size: 25px;
    font-weight: 500;
    letter-spacing: 6px;
    color: var(--grey);
  }

  /* back */
  .back-mascot {
    position: absolute;
    left: 70px;
    top: 80px;
    width: 165px;
    height: 142px;
    border-radius: 44% 44% 40% 40%;
    background: radial-gradient(circle at 50% 50%, #3a3536 0%, var(--black) 72%);
  }
  .contact {
    position: absolute;
    right: 23px;
    top: 26px;
    text-align: right;
  }
  .contact__name { font-size: 29px; line-height: 32px; font-weight: 300; }
  .contact__name strong { font-weight: 700; }
  .contact__email { font-size: 16px; line-height: 20px; font-weight: 400; }

  .services {
    position: absolute;
    left: 259px;
    top: 100px;
    width: 214px;
  }
  .services__title {
    font-size: 15px;
    font-weight: 700;
    line-height: 18px;
    padding-bottom: 1px;
    border-bottom: 2px solid var(--orange);
  }
  .services__list {
    list-style: none;
    margin-top: 5px;
    font-size: 13px;
    line-height: 16.5px;
    font-weight: 500;
    width: 195px;
  }
  .services__list li { display: inline; }
  .services__list .dot { color: var(--orange); padding: 0 1px; }

  .back-phone {
    position: absolute;
    right: 23px;
    top: 182px;
    font-size: 35px;
    line-height: 40px;
    font-weight: 700;
  }
  .back-rule {
    position: absolute;
    left: 100px;
    right: 0;
    top: 222px;
    height: 3px;
    background: var(--orange);
  }
</style>
</head>
<body>
  <div class="side-label side-label--front">FRONT</div>
  <div class="side-label side-label--back">BACK</div>

  <section class="card card--front">
    <svg class="card__shape" viewBox="0 0 473 270" aria-hidden="true">
      <polygon fill="var(--orange)" points="0,0 288,0 308,27 333,27 398,135 333,244 306,244 290,270 0,270"/>
    </svg>
    <div class="brand-name">Steadfast Vermin Guard</div>
    <div class="brand-mascot" role="img" aria-label="Cartoon insect mascot illustration"></div>
    <div class="front-phone">0461 275 804</div>
  </section>

  <section class="card card--back">
    <svg class="card__shape" viewBox="0 0 473 270" aria-hidden="true">
      <polygon fill="var(--orange)" points="0,0 184,0 163,27 113,27 49,135 113,244 163,244 183,270 0,270"/>
    </svg>
    <div class="back-mascot" role="img" aria-label="Cartoon insect mascot illustration"></div>
    <div class="contact">
      <div class="contact__name">Gavin <strong>Holloway</strong></div>
      <div class="contact__email">Info@steadfastverminguard.com.au</div>
    </div>
    <div class="services">
      <div class="services__title">SERVICES / INSPECTIONS</div>
      <ul class="services__list">
        <li>Termites</li> <li><span class="dot">•</span>Wood Borers</li> <li><span class="dot">•</span>Ants</li>
        <li>Cockroaches</li> <li><span class="dot">•</span>Spiders</li> <li><span class="dot">•</span>Fleas</li> <li><span class="dot">•</span>Mice</li>
        <li>Rats</li><li><span class="dot">•</span> Bed Bugs &nbsp;&amp; More!</li>
      </ul>
    </div>
    <div class="back-phone">0461 275 804</div>
    <div class="back-rule"></div>
  </section>
</body>
</html>
```